Business school needs a web design

Who We are:
KRVT is a small business school that offers programs in Project Management. The school is based in West Africa and welcomes students from the whole area. Our aim is to become one of the reference business schools in Africa.

Project Brief:
The site will include all informations relevant for different types of visitors that we have: actual and future students, companies, mass media, future employees, ect. It will present information about subscription, list of programs, presentation of the school and its team,etc.

What We want:
This competition is for Design only no coding! We need design for two pages.
We did some wireframing for the home page and the list of programs page. We made them just to show how we imagine the website would look like. But we encourage creative designs, so you don't have to stick to the wireframe models.

Sites We like:
http://www.ravenmoorcollege.example/
http://www.belvantis.example/fr/etudes.html
http://www.qtl.example/mba/Pages/default.aspx

Color schemes
The logo of the school is red and black. So the color scheme of the website should match that. For the rest, it is opened to your imagination.
Updates

The payment for the project is now garanteed. Good luck to you all !

Target Market(s)

The target market is diversified because we have students of different ages, also company representatives or employees that might visit the website for recruitment purposes. But the majority of our audience should be aged between 20 - 30 years.

Industry/Entity Type

Small Business

Requirements
Must have
• The design must include two pages: a home page and another interior page : might be the list of programs or any other page relevant to the domain. The Home page must include a slide show at the beginning.
The background page must be white.
Nice to have
• The use of flat design for this project is preferred.
The use of Pelican scaffold as a base for the design is an asset.

```html
<!DOCTYPE html>
<html lang="fr">
<head>
<meta charset="utf-8">
<title>KRVT – École de gestion</title>
<link rel="stylesheet" href="https://fonts.googleapis.com/css2?family=Bebas+Neue&family=Lato:wght@300;400&family=Roboto:wght@400;500&display=swap">
<style>
  :root {
    --white: #ffffff;
    --ink: #111111;
    --nav-bg: #151515;
    --brand-red: #c80d0d;
    --muted: #7a7a7a;
    --band: #4b4b4b;
    --search-bg: #e8e8e8;
    --search-line: #bdbdbd;
    --social-circle: #2c56d8;
    --social-chirp: #8e8e8e;
    --social-work: #7d7d7d;
    --social-print: #a4a4a4;
  }
  * { margin: 0; padding: 0; box-sizing: border-box; }
  html, body { width: 1200px; height: 900px; overflow: hidden; background: var(--white); }
  body { position: relative; font-family: "Lato", sans-serif; color: var(--ink); }

  .site-header { position: absolute; inset: 0 0 auto 0; height: 97px; }
  .brand-mark {
    position: absolute; left: 104px; top: 30px;
    font-family: "Roboto", sans-serif; font-weight: 500; font-size: 30px;
    color: var(--brand-red); letter-spacing: 1px;
  }
  .utility-links {
    position: absolute; right: 98px; top: 7px; list-style: none; display: flex;
    font-family: "Roboto", sans-serif; font-size: 15px; color: var(--muted);
  }
  .utility-links li + li::before { content: "|"; margin: 0 11px; }
  .search-box {
    position: absolute; left: 859px; top: 42px; width: 242px; height: 29px;
    background: var(--search-bg); border: 1px solid var(--search-line); border-radius: 3px;
  }
  .search-box .divider { position: absolute; left: 207px; top: 5px; width: 1px; height: 17px; background: #777; }
  .search-box svg { position: absolute; left: 215px; top: 6px; }

  .main-nav { position: absolute; left: 0; top: 97px; width: 1200px; height: 43px; background: var(--nav-bg); }
  .main-nav ul { list-style: none; }
  .main-nav li {
    position: absolute; top: 11px; font-family: "Roboto", sans-serif; font-weight: 500;
    font-size: 16px; color: var(--white); white-space: nowrap;
  }
  .main-nav .active-tab {
    position: absolute; left: 118px; top: 36px; width: 168px; height: 7px;
    background: var(--brand-red); border-radius: 5px 5px 0 0;
  }

  .hero-slide {
    position: absolute; left: 0; top: 140px; width: 1200px; height: 464px;
    background: linear-gradient(100deg, #eef2f4 0%, #dfe5ea 35%, #b9c0c7 60%, #3b3f46 85%, #e9ecef 100%);
  }
  .hero-name {
    position: absolute; left: 137px; top: 72px; font-family: "Bebas Neue", sans-serif;
    font-size: 52px; line-height: 60px; letter-spacing: 1.5px; color: var(--brand-red);
  }
  .hero-title {
    position: absolute; left: 137px; top: 157px; font-family: "Bebas Neue", sans-serif;
    font-weight: 400; font-size: 49px; line-height: 52px; letter-spacing: 1.5px; color: var(--ink);
  }
  .slide-arrow { position: absolute; top: 212px; }
  .slide-arrow.prev { left: 100px; }
  .slide-arrow.next { left: 1082px; }

  .intro-band {
    position: absolute; left: 80px; top: 604px; width: 1120px; height: 219px;
    padding-right: 50px; background: var(--band); color: var(--white); text-align: center;
  }
  .intro-band h1 { margin-top: 36px; font-weight: 300; font-size: 32px; letter-spacing: 0.3px; }
  .intro-band p { margin-top: 14px; font-size: 15.5px; line-height: 20px; }
  .more-button {
    position: absolute; left: 574px; top: 797px; width: 57px; height: 57px; border-radius: 50%;
    background: var(--brand-red); display: flex; align-items: center; justify-content: center;
  }

  .share-bar { position: absolute; left: 0; top: 604px; width: 80px; list-style: none; }
  .share-bar li {
    display: flex; align-items: center; justify-content: center; color: var(--white);
    font-family: "Lato", sans-serif; font-size: 12px;
  }
  .share-circlebook { height: 75px; background: var(--social-circle); }
  .share-chirper { height: 71px; background: var(--social-chirp); }
  .share-workweb { height: 75px; background: var(--social-work); }
  .share-print { height: 75px; background: var(--social-print); }
</style>
</head>
<body>
  <header class="site-header">
    <div class="brand-mark">KRVT</div>
    <ul class="utility-links">
      <li>Repertoire du personel</li>
      <li>Blogue</li>
      <li>Salle de presse</li>
      <li>Nous joindre</li>
      <li>Français</li>
    </ul>
    <div class="search-box">
      <span class="divider"></span>
      <svg width="20" height="16" viewBox="0 0 20 16"><circle cx="7" cy="6" r="4.5" fill="none" stroke="#666" stroke-width="2"/><line x1="10.5" y1="9" x2="16" y2="13" stroke="#666" stroke-width="3" stroke-linecap="round"/></svg>
    </div>
  </header>

  <nav class="main-nav">
    <ul>
      <li style="left:132px">A propos de l'KRVT</li>
      <li style="left:345px">Programmes et Formations</li>
      <li style="left:614px">Etudiant</li>
      <li style="left:746px">Novelles et Evenements</li>
      <li style="left:991px">Entreprises</li>
    </ul>
    <span class="active-tab"></span>
  </nav>

  <section class="hero-slide" role="img" aria-label="Photo of smiling business students in suits seated along a meeting table">
    <div class="hero-name">KRVT</div>
    <h2 class="hero-title">One of the best business<br>school of Africa</h2>
    <svg class="slide-arrow prev" width="20" height="42" viewBox="0 0 20 42"><polyline points="17,2 3,21 17,40" fill="none" stroke="#777" stroke-width="2"/></svg>
    <svg class="slide-arrow next" width="20" height="42" viewBox="0 0 20 42"><polyline points="3,2 17,21 3,40" fill="none" stroke="#bbb" stroke-width="2"/></svg>
  </section>

  <section class="intro-band">
    <h1>KRVT : DEVENEZ LES GESTIONNAIRES DE DEMAIN</h1>
    <p>Lorem ipsum dolor sit amet, consectetur adipiscing elit. Pellentesque sed eros at sem scelerisque varius at et lectus.<br>
    Etiam accumsan turpis orci, sed ultricies arcu imperdiet sed. Pellentesque suscipit libero non lacus gravida,<br>
    sit amet tempor diam hendrerit. Nunc ultricies mauris in odio cursus rhoncus. Nullam semper, quam vitae consequat luctus,<br>
    urna sem iaculis urna, ac auctor enim quam non odio.</p>
  </section>
  <a class="more-button" href="#" aria-label="En savoir plus">
    <svg width="30" height="18" viewBox="0 0 30 18"><line x1="1" y1="9" x2="28" y2="9" stroke="#fff" stroke-width="2"/><polyline points="20,1 28,9 20,17" fill="none" stroke="#fff" stroke-width="2"/></svg>
  </a>

  <ul class="share-bar">
    <li class="share-circlebook">Circlebook</li>
    <li class="share-chirper">Chirper</li>
    <li class="share-workweb">Workweb</li>
    <li class="share-print">
      <svg width="32" height="32" viewBox="0 0 32 32" aria-label="Imprimer"><rect x="9" y="2" width="14" height="8" fill="none" stroke="#fff" stroke-width="2"/><rect x="2" y="10" width="28" height="12" rx="2" fill="none" stroke="#fff" stroke-width="2"/><rect x="8" y="18" width="16" height="12" fill="var(--social-print)" stroke="#fff" stroke-width="2"/><line x1="11" y1="23" x2="21" y2="23" stroke="#fff" stroke-width="1.5"/><line x1="11" y1="26" x2="21" y2="26" stroke="#fff" stroke-width="1.5"/></svg>
    </li>
  </ul>
</body>
</html>
```